New Plumbing Company

We are looking for a smart and creative business card design for our new plumbing company. We are looking for creativity and originality in our business cards.

Industry/Entity Type

Plumbing

Contact Information for Business Card

Crestline Plumbing
Peter Halvane
Managing Director
Telephone Number : 0481529604
Email : service@crestlineplumbing.com.au
Website : www.crestlineplumbing.com.au
Lic. 508264K

Colors
0692cd
33a6d7
000000

Requirements
Must have
• I want the business card to be designed on a black background using the blue tones i have selected as seen in the company logo.

```html
<!DOCTYPE html>
<html lang="en">
<head>
<meta charset="utf-8">
<title>Crestline Plumbing – Business Card</title>
<link href="https://fonts.googleapis.com/css2?family=Roboto+Condensed:wght@300;400;700&display=swap" rel="stylesheet">
<style>
  :root {
    --blue-deep: #0692cd;
    --blue-light: #33a6d7;
    --black: #000000;
    --card-black: #0b0b0c;
    --text-soft: #d6d9dc;
    --line-grey: #bfc4c8;
    --stage: #e8e6e3;
  }
  * { margin: 0; padding: 0; box-sizing: border-box; }
  html, body { width: 1200px; height: 1000px; overflow: hidden; }
  body {
    background: var(--stage);
    font-family: "Roboto Condensed", Arial, sans-serif;
    position: relative;
  }
  .card {
    position: absolute;
    left: 250px;
    width: 700px;
    height: 400px;
    border-radius: 4px;
    overflow: hidden;
    background: linear-gradient(160deg, #1c1c1e 0%, var(--card-black) 45%, var(--black) 100%);
    box-shadow: 0 10px 28px rgba(0,0,0,.25);
  }
  .card--front { top: 60px; }
  .card--back  { top: 540px; }

  /* Front */
  .front-brand {
    position: absolute;
    left: 150px; top: 160px;
    display: flex; align-items: center; gap: 22px;
  }
  .brand-dot {
    width: 64px; height: 64px; border-radius: 50%;
    border: 5px solid var(--blue-light);
  }
  .brand-name {
    font-size: 56px; font-weight: 300; letter-spacing: 1px;
    color: var(--blue-light); line-height: 1;
  }
  .front-web {
    position: absolute; right: 40px; bottom: 34px;
    font-size: 22px; font-weight: 300; color: var(--text-soft);
    letter-spacing: .5px;
  }

  /* Back */
  .back-band {
    position: absolute; left: 0; top: 0; width: 100%; height: 86px;
    background: linear-gradient(90deg, var(--blue-light), #48b6e2 60%, var(--blue-light));
    display: flex; align-items: center; justify-content: space-between;
    padding: 0 40px;
  }
  .holder-name { font-size: 34px; font-weight: 300; color: #eef8fd; }
  .holder-role { font-size: 24px; font-weight: 300; color: #eef8fd; }
  .back-strip {
    position: absolute; left: 0; top: 86px; width: 100%; height: 24px;
    background: var(--blue-deep);
  }
  .back-links { position: absolute; left: 0; top: 0; }
  .contact-list {
    position: absolute; left: 205px; top: 142px;
    list-style: none;
  }
  .contact-list li {
    font-size: 25px; font-weight: 300; color: #f0f2f4;
    height: 40px; line-height: 36px; letter-spacing: .3px;
  }
  .back-brand {
    position: absolute; left: 40px; bottom: 36px;
    display: flex; align-items: center; gap: 12px;
  }
  .back-brand .brand-dot { width: 30px; height: 30px; border-width: 3px; }
  .back-brand .brand-name { font-size: 28px; }
  .licence {
    position: absolute; right: 40px; bottom: 34px;
    font-size: 26px; font-weight: 700; color: #ffffff; letter-spacing: 1px;
  }
</style>
</head>
<body>

<section class="card card--front" aria-label="Business card front">
  <div class="front-brand">
    <span class="brand-dot"></span>
    <span class="brand-name">Crestline Plumbing</span>
  </div>
  <p class="front-web">www.crestlineplumbing.com.au</p>
</section>

<section class="card card--back" aria-label="Business card back">
  <div class="back-band">
    <span class="holder-name">Peter Halvane</span>
    <span class="holder-role">Managing Director</span>
  </div>
  <div class="back-strip"></div>

  <svg class="back-links" width="700" height="400" viewBox="0 0 700 400" aria-hidden="true">
    <g fill="none" stroke="var(--line-grey)" stroke-width="1.5">
      <polyline points="150,110 150,160 192,160"/>
      <polyline points="110,110 110,200 192,200"/>
      <polyline points="70,110 70,240 192,240"/>
    </g>
    <g fill="#ffffff">
      <circle cx="194" cy="160" r="3.5"/>
      <circle cx="194" cy="200" r="3.5"/>
      <circle cx="194" cy="240" r="3.5"/>
    </g>
    <!-- icons on strip -->
    <g stroke="#ffffff" stroke-width="1.6" fill="var(--blue-deep)">
      <circle cx="70" cy="98" r="13"/>
      <circle cx="110" cy="98" r="13"/>
      <circle cx="150" cy="98" r="13"/>
    </g>
    <g stroke="#ffffff" stroke-width="1.2" fill="none">
      <!-- globe -->
      <circle cx="70" cy="98" r="7"/>
      <ellipse cx="70" cy="98" rx="3" ry="7"/>
      <line x1="63" y1="98" x2="77" y2="98"/>
      <!-- mail -->
      <rect x="103" y="93" width="14" height="10"/>
      <polyline points="103,93 110,99 117,93"/>
      <!-- phone -->
      <rect x="146" y="90" width="8" height="15" rx="1.5"/>
      <line x1="148.5" y1="102" x2="151.5" y2="102"/>
    </g>
  </svg>

  <ul class="contact-list">
    <li>0481529604</li>
    <li>service@crestlineplumbing.com.au</li>
    <li>www.crestlineplumbing.com.au</li>
  </ul>

  <div class="back-brand">
    <span class="brand-dot"></span>
    <span class="brand-name">Crestline Plumbing</span>
  </div>
  <p class="licence">Lic. 508264K</p>
</section>

</body>
</html>
```